Business Cards Design for the electrical wholesaler: clean bold dynamic :)

We need a business card design that would follow our latest brand guidelines. As an electrical wholesaler we want to bring a fresh look and feel into the industry. The design should be clean bold and dynamic. It should come alive with the renewed energy of our green colour. Our grey colour should keep things balanced and complement the notion of maturity and responsibility. We employ Lato as a corporate font however are not bound by this font and we’re open to interpretation here.

Target Market(s)

Electrical contractors

Industry/Entity Type

Business

Contact Information for Business Card

Logo
Name & Surname: Olena Dovbush
Job Title: Director of Marketing
Email: helen.dovbush@mailvane.example
Cell phone: XXX.XXX.XXXX
Address: 20917 - 87 Ave. Edmonton, AB, Canada. T6K 2R8
Business Phone: 780.555.0187
Website: www.qorvil.example

Font styles to use
Other font styles liked:
• Lato

Requirements
Must have
• Logo & website
Nice to have
• Brand elements - some of them you may find in the attached Brand Guidelines (e.g. three lines on the background signifying "W")

```html
<!DOCTYPE html>
<html lang="en">
<head>
<meta charset="utf-8">
<title>Qorvil Business Card</title>
<link href="https://fonts.googleapis.com/css2?family=Lato:wght@400;700;900&family=Roboto+Condensed:wght@300;400&display=swap" rel="stylesheet">
<style>
  :root {
    --green: #72b44b;
    --green-deep: #5d8a3f;
    --charcoal: #1f2220;
    --slate: #373b45;
    --grey: #505254;
    --paper: #ffffff;
    --backdrop: #ececec;
  }
  html, body {
    margin: 0;
    width: 1200px;
    height: 1200px;
    overflow: hidden;
    background: var(--backdrop);
  }
  .card {
    position: absolute;
    left: 186px;
    width: 823px;
    height: 470px;
    background: var(--paper);
    overflow: hidden;
  }
  .card--front { top: 58px; }
  .card--back { top: 666px; }

  /* front */
  .brand {
    position: absolute;
    top: 150px;
    left: 0;
    width: 100%;
    display: flex;
    justify-content: center;
    align-items: center;
    gap: 26px;
  }
  .brand__square {
    width: 72px;
    height: 72px;
    background: var(--green);
  }
  .brand__name {
    font-family: "Lato", sans-serif;
    font-weight: 400;
    font-size: 110px;
    line-height: 1;
    color: var(--grey);
    letter-spacing: -1px;
  }
  .band-dark {
    position: absolute;
    left: 0;
    top: 350px;
    width: 100%;
    height: 120px;
    background: var(--charcoal);
  }
  .block {
    position: absolute;
    box-sizing: border-box;
    border: 5px solid var(--paper);
  }
  .block--left { left: -5px; top: 305px; width: 119px; height: 103px; background: var(--green-deep); border-top: 0; }
  .block--centre { left: 286px; top: 305px; width: 246px; height: 103px; background: var(--green); border-top: 0; }
  .block--low { left: 152px; top: 444px; width: 108px; height: 36px; background: var(--green); }
  .block--right { left: 716px; top: 404px; width: 112px; height: 76px; background: var(--green-deep); }

  /* back */
  .person {
    position: absolute;
    top: 76px;
    left: 0;
    width: 100%;
    text-align: center;
    font-family: "Roboto Condensed", sans-serif;
  }
  .person__name {
    margin: 0;
    font-weight: 300;
    font-size: 46px;
    line-height: 1;
    color: var(--charcoal);
    letter-spacing: -0.5px;
  }
  .person__surname { color: var(--green); font-weight: 400; }
  .person__role {
    margin: 18px 0 0;
    font-weight: 400;
    font-size: 22px;
    color: var(--charcoal);
    letter-spacing: -0.5px;
  }
  .contact-band {
    position: absolute;
    left: 0;
    top: 230px;
    width: 100%;
    height: 240px;
    display: grid;
    grid-template-columns: 412px 411px;
    grid-template-rows: 120px 120px;
  }
  .contact-band__cell--dark { background: var(--charcoal); }
  .contact-band__cell--slate { background: var(--slate); }
  .contact-text {
    position: absolute;
    color: var(--paper);
    white-space: nowrap;
  }
  .contact-text--email {
    left: 72px; top: 65px;
    font-family: "Lato", sans-serif;
    font-size: 17px;
  }
  .contact-text--web {
    left: 72px; top: 177px;
    font-family: "Lato", sans-serif;
    font-weight: 900;
    font-size: 15px;
    letter-spacing: 2.4px;
    text-transform: uppercase;
  }
  .contact-text--phones, .contact-text--address {
    left: 532px;
    font-family: "Roboto Condensed", sans-serif;
    font-size: 17px;
    line-height: 16px;
  }
  .contact-text--phones { top: 58px; }
  .contact-text--address { top: 140px; }
  .icon-grid {
    position: absolute;
    left: 330px;
    top: 38px;
    width: 164px;
    height: 164px;
    display: grid;
    grid-template-columns: 1fr 1fr;
    grid-template-rows: 1fr 1fr;
    gap: 4px;
    padding: 4px;
    box-sizing: border-box;
    background: var(--paper);
  }
  .icon-tile {
    display: flex;
    align-items: center;
    justify-content: center;
  }
  .icon-tile--light { background: var(--green); }
  .icon-tile--deep { background: var(--green-deep); }
  .icon-tile svg { width: 24px; height: 24px; }
</style>
</head>
<body>

<section class="card card--front" aria-label="Card front">
  <div class="brand">
    <span class="brand__square"></span>
    <span class="brand__name">qorvil</span>
  </div>
  <div class="band-dark"></div>
  <div class="block block--left"></div>
  <div class="block block--centre"></div>
  <div class="block block--low"></div>
  <div class="block block--right"></div>
</section>

<section class="card card--back" aria-label="Card back">
  <div class="person">
    <h1 class="person__name">OLENA <span class="person__surname">DOVBUSH</span></h1>
    <p class="person__role">DIRECTOR OF MARKETING</p>
  </div>

  <div class="contact-band">
    <div class="contact-band__cell--dark"></div>
    <div class="contact-band__cell--slate"></div>
    <div class="contact-band__cell--slate"></div>
    <div class="contact-band__cell--dark"></div>

    <span class="contact-text contact-text--email">helen.dovbush@mailvane.example</span>
    <span class="contact-text contact-text--web">www.qorvil.example</span>
    <span class="contact-text contact-text--phones">780.555.0187<br>XXX.XXX.XXXX</span>
    <span class="contact-text contact-text--address">20917 - 87<br>Ave. Edmonton, AB, Canada. T6K 2R8</span>

    <div class="icon-grid">
      <div class="icon-tile icon-tile--light">
        <svg viewBox="0 0 24 24" aria-label="Email">
          <path d="M3 10 L12 4 L21 10 V20 H3 Z" fill="#fff"/>
          <path d="M3 10 L12 15 L21 10" fill="none" stroke="#72b44b" stroke-width="1.5"/>
          <path d="M3 20 L10 14 M21 20 L14 14" stroke="#72b44b" stroke-width="1.2"/>
        </svg>
      </div>
      <div class="icon-tile icon-tile--deep">
        <svg viewBox="0 0 24 24" aria-label="Phone book">
          <rect x="5" y="3" width="14" height="18" rx="1" fill="#fff"/>
          <circle cx="12" cy="10" r="2.4" fill="#5d8a3f"/>
          <path d="M8 16 Q12 11.5 16 16 Z" fill="#5d8a3f"/>
        </svg>
      </div>
      <div class="icon-tile icon-tile--deep">
        <svg viewBox="0 0 24 24" aria-label="Website">
          <circle cx="12" cy="12" r="9" fill="#fff"/>
          <path d="M7 8 Q10 6 12 9 Q11 12 8 12 Z M13 14 Q16 12 17 15 Q15 19 13 18 Z M14 5 Q17 6 18 9 Q15 9 14 5 Z" fill="#5d8a3f"/>
        </svg>
      </div>
      <div class="icon-tile icon-tile--light">
        <svg viewBox="0 0 24 24" aria-label="Address">
          <path d="M2 12 L12 3 L22 12 L20 13.5 L12 6.5 L4 13.5 Z" fill="#fff"/>
          <path d="M5.5 13 L12 7.5 L18.5 13 V21 H5.5 Z" fill="#fff"/>
          <rect x="10" y="15" width="4" height="6" fill="#72b44b"/>
          <rect x="16" y="4" width="2.5" height="5" fill="#fff"/>
        </svg>
      </div>
    </div>
  </div>
</section>

</body>
</html>
```